UK Glass Restoration Company needs a Direct Mail Postcard Design

We need a HARD HITTING, COMPELLING 300dpi Camera Ready double sided postcard.
The dimensions will be 109mm x 152mm including bleed. We are a scratched glass repair / etched graffiti removal glass restoration company based in London, UK.
We operate mainly within the construction and commercial marketplace, however this particular postcard design is aimed solely at shop owners who have become victims of vandalism, due to etched graffiti tags and or scratches being left on their shop front glass.
We wish to focus the shop / business owners mind to the negative impact such vandalism has on the image of their business and how we are able to offer a quick and cost effective solution
We will supply text for both sides of the postcard along with relevant images, company logo and previous flyer designs, however we are happy for the selected designer to source suitable alternative images provided they are in keeping with the exact "Before" and "After" theme.
The finished postcard must preferably have a white background, but again we are open to creative suggestions.
Target Market(s)
UK SHOP OWNERS
Industry/Entity Type
It Company

```html
<!DOCTYPE html>
<html lang="en">
<head>
<meta charset="utf-8">
<title>Lumina Glass Care – Shop Window Postcard</title>
<link href="https://fonts.googleapis.com/css2?family=Open+Sans:wdth,wght@75..100,300..800&family=Arimo:wght@700&display=swap" rel="stylesheet">
<style>
  :root{
    --page:#eeeeee;
    --white:#ffffff;
    --blue-light:#3a9ad0;
    --brand-blue:#1a86c8;
    --navy:#164b8a;
    --grey:#b9b9bd;
    --grey-dark:#6d6d72;
    --text-dark:#222222;
  }
  *{box-sizing:border-box;margin:0;padding:0}
  html,body{width:900px;height:1200px;overflow:hidden;background:var(--page)}
  body{position:relative;font-family:"Open Sans",Arial,sans-serif}

  .postcard{position:absolute;left:60px;width:780px;height:560px;overflow:hidden;
    box-shadow:0 4px 14px rgba(0,0,0,.25);background:var(--white)}
  .postcard--front{top:27px}
  .postcard--back{top:613px}
  .postcard__shapes{position:absolute;inset:0}

  .portrait{position:absolute;border-radius:50%;border:7px solid var(--blue-light);
    box-shadow:0 0 0 3px var(--white);
    background:radial-gradient(circle at 50% 45%,#b8c3c8,#5d6a70 70%,#3e4a50)}
  .postcard--front .portrait{left:16px;top:16px;width:156px;height:156px}
  .postcard--back .portrait{left:18px;top:20px;width:158px;height:158px;
    background:radial-gradient(circle at 55% 50%,#9aa6ad,#56636a 70%,#3c474d)}

  .brand{position:absolute;display:flex;flex-direction:column;align-items:flex-start;color:var(--brand-blue)}
  .brand__name{font-size:48px;font-weight:400;line-height:1;letter-spacing:-.5px}
  .brand__tag{font-size:14px;font-weight:400;letter-spacing:3px;margin-left:4px;line-height:1.1}
  .postcard--front .brand{left:322px;top:34px}
  .postcard--back .brand{left:298px;top:42px}
  .postcard--back .brand__name{font-size:56px}
  .postcard--back .brand__tag{font-size:16px}

  .headline{position:absolute;left:198px;top:112px;font-family:"Arimo",Arial,sans-serif;
    font-weight:700;font-size:19px;color:var(--grey-dark);white-space:nowrap;letter-spacing:.1px}
  .headline strong{color:var(--navy)}

  .intro{position:absolute;left:38px;top:222px;width:300px;color:var(--white);
    font-size:12px;line-height:1.36}

  .call{position:absolute;left:38px;top:388px;width:300px;text-align:center;color:var(--white)}
  .call__label{font-family:"Arimo",Arial,sans-serif;font-size:20px;font-weight:700}
  .call__number{font-family:"Arimo",Arial,sans-serif;font-size:34px;font-weight:700;margin-top:4px;letter-spacing:.5px}

  .why{position:absolute;left:42px;top:182px;color:var(--white);
    font-family:"Arimo",Arial,sans-serif;font-size:20px;font-weight:700}
  .benefits{position:absolute;left:36px;top:212px;width:300px;list-style:none;color:var(--white);
    font-size:11.8px;line-height:1.18}
  .benefits li{position:relative;padding-left:16px;margin-bottom:6px;text-align:justify}
  .benefits li::before{content:"";position:absolute;left:0;top:4px;width:8px;height:8px;border-radius:50%;background:var(--white)}

  .badge{position:absolute;width:126px;height:126px;border-radius:50%;background:var(--white);
    border:6px solid #8e8f94;box-shadow:0 0 0 2px var(--white),0 3px 8px rgba(0,0,0,.35);
    display:flex;flex-direction:column;align-items:center;justify-content:center;text-align:center;
    color:var(--brand-blue);font-weight:700;font-stretch:78%;line-height:1.12}
  .postcard--front .badge{left:348px;top:320px}
  .postcard--back .badge{left:346px;top:304px}
  .badge__small{font-size:17px}
  .badge__big{font-size:20px}

  .contact{position:absolute;left:0;width:338px;height:58px;background:var(--white);
    border-radius:0 29px 29px 0;padding:8px 0 0 40px;color:var(--text-dark);box-shadow:0 -2px 0 var(--grey)}
  .postcard--front .contact{top:472px}
  .postcard--back .contact{top:466px;left:18px}
  .contact__row{display:flex;align-items:center;gap:12px;height:21px}
  .contact__web{font-size:12.5px}
  .contact__phone{font-size:16px}
  .contact svg{width:14px;height:14px;flex:none}
</style>
</head>
<body>

<section class="postcard postcard--front">
  <svg class="postcard__shapes" viewBox="0 0 780 560">
    <defs>
      <linearGradient id="front-blue" x1="0" y1="0" x2="1" y2="1">
        <stop offset="0" stop-color="#2b8fc9"/><stop offset=".6" stop-color="#1a76ad"/><stop offset="1" stop-color="#0f5f92"/>
      </linearGradient>
      <linearGradient id="front-photo" x1="0" y1="0" x2="1" y2="1">
        <stop offset="0" stop-color="#4b3626"/><stop offset=".5" stop-color="#8c7a68"/><stop offset="1" stop-color="#5a4634"/>
      </linearGradient>
    </defs>
    <rect width="780" height="560" fill="url(#front-blue)"/>
    <path role="img" aria-label="Photo of a scratched, graffiti-etched shop window with property listings behind" d="M375,560 C392,420 450,290 560,232 L780,170 V560 Z" fill="url(#front-photo)"/>
    <path d="M375,560 C392,420 450,290 560,232 L780,170" fill="none" stroke="#111" stroke-width="8"/>
    <path d="M365,560 C382,418 440,284 552,225" fill="none" stroke="#fff" stroke-width="3"/>
    <path d="M120,0 H780 V150 C690,205 590,232 480,236 C330,242 210,175 150,70 Z" fill="#111"/>
    <path d="M120,0 H780 V138 C690,195 590,222 480,226 C330,232 210,165 150,62 Z" fill="#c6c6ca"/>
    <path d="M120,0 H780 V118 C690,178 590,204 480,208 C330,214 215,150 160,55 Z" fill="#fff"/>
    <path d="M660,308 L720,280 V296 H780 V332 H720 V348 Z" fill="#1a8ed4"/>
  </svg>
  <div class="portrait" role="img" aria-label="Photo of a technician in a hi-vis vest repairing a shop window"></div>
  <div class="brand"><span class="brand__name">Lumina</span><span class="brand__tag">glass care</span></div>
  <h1 class="headline"><strong>DON'T LET VANDALS</strong> WRECK YOUR IMAGE!</h1>
  <p class="intro">What's on display in your shop window? If it's graffiti, vandalism, or just wear and tear, that's the first impression your customers get – and it's not good.<br>Lumina Glass Care remove damage from glass windows, making them sparkling clear – without replacing the glass! Our glass repair work is effective, green, and very economical. See our coupon on the other side to save even more!</p>
  <div class="call"><div class="call__label">Call now for expert advice</div><div class="call__number">0800 555 0137</div></div>
  <div class="badge"><span class="badge__small">Before repair</span><span class="badge__big">a bad first<br>impression</span></div>
  <div class="contact">
    <div class="contact__row"><svg viewBox="0 0 14 14"><circle cx="7" cy="7" r="6" fill="var(--navy)"/><path d="M1,7H13M7,1C4,4 4,10 7,13M7,1C10,4 10,10 7,13" stroke="#fff" fill="none" stroke-width="1"/></svg><span class="contact__web">www.luminaglasscare.co.uk</span></div>
    <div class="contact__row"><svg viewBox="0 0 14 14"><rect x="1" y="1" width="12" height="12" rx="2" fill="var(--navy)"/><path d="M5,4 L6,6 L5.5,7 C6,8 6.5,8.5 7.5,9 L8.5,8.5 L10,9.5 L9,11 C6,10.5 4,8 3.5,5 Z" fill="#fff"/></svg><span class="contact__phone">0800 555 0137</span></div>
  </div>
</section>

<section class="postcard postcard--back">
  <svg class="postcard__shapes" viewBox="0 0 780 560">
    <defs>
      <linearGradient id="back-blue" x1="0" y1="0" x2="1" y2="1">
        <stop offset="0" stop-color="#2b8fc9"/><stop offset=".6" stop-color="#1a76ad"/><stop offset="1" stop-color="#0f5f92"/>
      </linearGradient>
      <linearGradient id="back-photo" x1="0" y1="0" x2="1" y2="1">
        <stop offset="0" stop-color="#a59888"/><stop offset=".5" stop-color="#d3cbc0"/><stop offset="1" stop-color="#8d7d6b"/>
      </linearGradient>
    </defs>
    <rect width="780" height="560" fill="url(#back-blue)"/>
    <path role="img" aria-label="Photo of the same shop window after repair, clear glass with property listings behind" d="M360,560 C380,400 440,250 580,150 L780,70 V560 Z" fill="url(#back-photo)"/>
    <path d="M360,560 C380,400 440,250 580,150 L780,70" fill="none" stroke="#111" stroke-width="8"/>
    <path d="M350,560 C370,398 430,245 572,143" fill="none" stroke="#fff" stroke-width="3"/>
    <path d="M110,0 H780 V60 C690,120 580,150 460,150 C330,150 220,120 160,60 Z" fill="#111"/>
    <path d="M110,0 H780 V50 C690,110 580,140 460,140 C330,140 220,110 160,50 Z" fill="#c6c6ca"/>
    <path d="M110,0 H780 V32 C690,95 580,122 460,122 C330,122 225,95 170,40 Z" fill="#fff"/>
    <path d="M628,290 L690,262 V278 H780 V312 H690 V328 Z" fill="#1a8ed4"/>
  </svg>
  <div class="portrait" role="img" aria-label="Photo of a technician in a hi-vis jacket polishing glass high above a city"></div>
  <div class="brand"><span class="brand__name">Lumina</span><span class="brand__tag">glass care</span></div>
  <h2 class="why">Why Lumina Glass Care?</h2>
  <ul class="benefits">
    <li>We repair most shop window glass! We repair laminated, tempered, toughened, mirrored, tinted, and even ballistic glass.</li>
    <li>We repair curved glass! Don't replace expensive curved panes – get the like-new look for less by repairing.</li>
    <li>Finer work! We remove etched graffiti tags, scratches, mineral deposits, and acid etched graffiti damage.</li>
    <li>Edge expertise! We can repair even deep scratches as close as 20mm from the edge of the glass.</li>
    <li>Save time and money! Typical savings of up to 80% over the cost of glass replacement, with zero downtime during repair.</li>
  </ul>
  <div class="badge"><span class="badge__big">After repair<br>clear as new!</span></div>
  <div class="contact">
    <div class="contact__row"><svg viewBox="0 0 14 14"><circle cx="7" cy="7" r="6" fill="var(--navy)"/><path d="M1,7H13M7,1C4,4 4,10 7,13M7,1C10,4 10,10 7,13" stroke="#fff" fill="none" stroke-width="1"/></svg><span class="contact__web">www.luminaglasscare.co.uk</span></div>
    <div class="contact__row"><svg viewBox="0 0 14 14"><rect x="1" y="1" width="12" height="12" rx="2" fill="var(--navy)"/><path d="M5,4 L6,6 L5.5,7 C6,8 6.5,8.5 7.5,9 L8.5,8.5 L10,9.5 L9,11 C6,10.5 4,8 3.5,5 Z" fill="#fff"/></svg><span class="contact__phone">0800 555 0137</span></div>
  </div>
</section>

</body>
</html>
```